Breezeway Comfort business cards design

Need a business card design for a Heating and Air Conditioning business. I need these items included.
Business name: Breezeway Comfort
Owner: Marcus Tollefsen
License # 2874590
Phone number # 555-382-4071
Email: breezewaycomfortair@mailvista.example
Sales
Service
Installation
Maintenance

Heating and Air Conditioning

Requirements
Must have
• Company name , license number , phone number , email

```html
<!DOCTYPE html>
<html lang="en">
<head>
<meta charset="utf-8">
<title>Breezeway Comfort – Business Cards</title>
<link href="https://fonts.googleapis.com/css2?family=Montserrat:wght@400;500;700;800&display=swap" rel="stylesheet">
<style>
  :root {
    --backdrop: #1c1c1d;
    --paper: #f3f3f3;
    --brand-blue: #1a44a0;
    --brand-orange: #ea6a2c;
    --ink: #333a44;
    --white: #ffffff;
    --faint-peach: #f5dcc4;
    --faint-pink: #f4d2d8;
    --faint-ice: #cdd7e8;
  }
  * { box-sizing: border-box; margin: 0; padding: 0; }
  html, body {
    width: 1200px; height: 1059px; overflow: hidden;
    background: var(--backdrop);
    font-family: "Montserrat", sans-serif;
  }
  .card {
    position: absolute;
    border-radius: 20px;
    overflow: hidden;
  }
  .card--front {
    left: 257px; top: 89px; width: 687px; height: 390px;
    background: var(--paper);
  }
  .card--back {
    left: 254px; top: 547px; width: 693px; height: 393px;
    background: var(--brand-blue);
  }

  /* Front */
  .front__brand {
    position: absolute; left: 38px; top: 68px;
    font-weight: 800; font-size: 33px; line-height: 1.02;
    color: var(--brand-blue); letter-spacing: 1.5px;
    text-transform: uppercase;
  }
  .front__decor {
    position: absolute; left: 372px; top: 20px;
    width: 292px; height: 350px;
    border-radius: 48% 52% 46% 54% / 42% 40% 60% 58%;
    background:
      radial-gradient(ellipse 60% 45% at 30% 28%, var(--faint-peach) 0%, transparent 70%),
      radial-gradient(ellipse 45% 55% at 42% 72%, var(--faint-pink) 0%, transparent 70%),
      radial-gradient(ellipse 45% 50% at 78% 62%, var(--faint-ice) 0%, transparent 72%);
    opacity: 0.9;
  }
  .owner {
    position: absolute; left: 39px; top: 205px; color: var(--ink);
  }
  .owner__name {
    font-weight: 700; font-size: 23px; color: var(--brand-blue);
    letter-spacing: 0.6px; line-height: 1.1;
  }
  .owner__role { font-size: 16px; letter-spacing: 0.5px; margin-top: 1px; }
  .owner__license { font-size: 16px; letter-spacing: 0.4px; margin-top: 17px; }
  .contact { list-style: none; margin-top: 17px; }
  .contact__item {
    display: flex; align-items: center; gap: 8px;
    font-size: 16.5px; letter-spacing: 0.4px; height: 25px;
  }
  .contact__icon { width: 13px; height: 13px; flex: none; }

  /* Back */
  .back__brand {
    position: absolute; left: 0; right: 0; top: 140px;
    display: flex; align-items: center; justify-content: center; gap: 22px;
  }
  .back__mark {
    width: 112px; height: 112px; border-radius: 50%;
    background: var(--brand-orange); flex: none;
  }
  .back__name {
    font-weight: 800; font-size: 48px; line-height: 1.02;
    color: var(--white); letter-spacing: 2px; text-transform: uppercase;
  }
  .services {
    position: absolute; left: 0; right: 0; top: 332px;
    display: flex; justify-content: center; align-items: center; gap: 9px;
    list-style: none; color: var(--white); font-size: 17px; letter-spacing: 0.4px;
  }
  .services__sep {
    width: 2px; height: 10px; background: var(--brand-orange);
  }
</style>
</head>
<body>
  <section class="card card--front" aria-label="Business card front">
    <div class="front__decor" role="img" aria-label="Faint brand emblem watermark in warm peach, pink and icy blue tones"></div>
    <div class="front__brand">Breezeway<br>Comfort</div>
    <div class="owner">
      <h1 class="owner__name">MARCUS TOLLEFSEN</h1>
      <p class="owner__role">Owner</p>
      <p class="owner__license">License # 2874590</p>
      <ul class="contact">
        <li class="contact__item">
          <svg class="contact__icon" viewBox="0 0 24 24" aria-hidden="true"><path fill="var(--brand-orange)" d="M6.6 10.8a15.1 15.1 0 0 0 6.6 6.6l2.2-2.2a1 1 0 0 1 1-.25 11.4 11.4 0 0 0 3.6.57 1 1 0 0 1 1 1V20a1 1 0 0 1-1 1A17 17 0 0 1 3 4a1 1 0 0 1 1-1h3.5a1 1 0 0 1 1 1c0 1.250.2 2.450.57 3.57a1 1 0 0 1-.25 1z"/></svg>
          <span>555-382-4071</span>
        </li>
        <li class="contact__item">
          <svg class="contact__icon" viewBox="0 0 24 24" aria-hidden="true"><rect x="1" y="4" width="22" height="16" fill="var(--brand-orange)"/><path d="M2 5l10 8 10-8" fill="none" stroke="var(--paper)" stroke-width="2"/></svg>
          <span>breezewaycomfortair@mailvista.example</span>
        </li>
      </ul>
    </div>
  </section>

  <section class="card card--back" aria-label="Business card back">
    <div class="back__brand">
      <span class="back__mark" aria-hidden="true"></span>
      <span class="back__name">Breezeway<br>Comfort</span>
    </div>
    <ul class="services">
      <li>Sales</li><li class="services__sep" aria-hidden="true"></li>
      <li>Service</li><li class="services__sep" aria-hidden="true"></li>
      <li>Installation</li><li class="services__sep" aria-hidden="true"></li>
      <li>Maintenance</li>
    </ul>
  </section>
</body>
</html>
```